Interior Decorating business - Logo & Stationery

"Velvet Lantern" is a newly established interior decorating company, based in Sydney, providing interior decorating, colour consulting and property styling services to residential and commercial clients.

We require a logo and stationery design (double-sided business card, A4 letterhead and with compliments slip (210mm X 95mm))

Letterhead information and with compliments slip:
Address - 22/31-33 Thornbury Rd, Kelvin Grove NSW 2098
Phone - (02)9617 4280
Mobile - 0427 386 509
Email - maeve@velvetlantern.com.au
Web - www.velvetlantern.com.au
ABN - 47392815064

Business Cards should be double sided and are to include;
Maeve Hollis
Director

with email address, mobile number, website as listed above

They also need to include services offered i.e. Interior Decorating, Colour Consulting, Property Styling

Please note that the current content on the website will be updated, so disregard logo and content currently on the website.

Target Market(s)

Target market is two-fold - residential clients (primarily homeowners with pride in their homes) and commerical clients (specifically business owners of retail shops and cafes and property developers)

Industry/Entity Type

Residential

```html
<!DOCTYPE html>
<html lang="en">
<head>
<meta charset="utf-8">
<title>Velvet Lantern – Logo &amp; Stationery</title>
<link rel="stylesheet" href="https://fonts.googleapis.com/css2?family=Cormorant+Garamond:wght@400;500&display=swap">
<style>
:root{
  --ink:#231f20;
  --accent:#a3262e;
  --rule:#2b2b2b;
  --paper:#ffffff;
  --damask:#e4e4e4;
  --damask-soft:#eeeeee;
  --label:#3a3a3a;
}
*{margin:0;padding:0;box-sizing:border-box}
html,body{width:1200px;height:600px;overflow:hidden;background:var(--paper)}
body{position:relative;font-family:"Cormorant Garamond",Georgia,serif;color:var(--ink)}
.caps{font-variant:small-caps;text-transform:lowercase;letter-spacing:.28em}
.abs{position:absolute}
.label{position:absolute;color:var(--label);font-size:12px;letter-spacing:.3em;font-variant:small-caps;text-transform:lowercase}
.label.big{font-size:22px;letter-spacing:.35em}
.sheet{position:absolute;background:var(--paper);border:1px solid #9a9a9a}
.card{border:1px solid var(--ink)}
.damask{position:absolute;background:radial-gradient(ellipse at 50% 45%,var(--damask) 0%,var(--damask) 55%,var(--damask-soft) 80%,transparent 100%);border-radius:40% 40% 30% 30%}
.damask-field{position:absolute;background:linear-gradient(180deg,var(--damask-soft),var(--damask),var(--damask-soft))}
.brand{position:absolute;display:flex;align-items:center;gap:.45em;white-space:nowrap;font-weight:400;color:var(--ink);letter-spacing:.12em}
.brand .mark{display:inline-block;width:.32em;height:.32em;background:var(--accent)}
.center{text-align:center;white-space:nowrap}
.redline{position:absolute;width:2px;background:var(--accent)}
.tiny-dot{display:inline-block;width:6px;height:6px;background:var(--accent)}
</style>
</head>
<body>

<!-- Logo -->
<div class="label big" style="left:32px;top:34px">logo</div>
<div class="brand" style="left:80px;top:70px;font-size:54px"><span>Velvet Lantern</span><span class="mark"></span></div>

<!-- Business card side 1 -->
<div class="label" style="left:32px;width:252px;top:194px;text-align:center">business card side 1</div>
<section class="sheet card" style="left:32px;top:222px;width:252px;height:145px">
  <div class="damask" role="img" aria-label="Faint damask ornament" style="left:150px;top:4px;width:90px;height:120px"></div>
  <div class="brand" style="left:18px;top:32px;font-size:20px"><span>Velvet Lantern</span><span class="mark"></span></div>
  <div class="abs center caps" style="left:0;width:252px;top:70px;font-size:13px">Maeve Hollis</div>
  <div class="abs center caps" style="left:0;width:252px;top:88px;font-size:8px">director</div>
  <div class="abs center" style="left:0;width:252px;top:104px;font-size:15px;letter-spacing:.25em">0427 386 509</div>
  <div class="abs center caps" style="left:0;width:252px;top:128px;font-size:9px;letter-spacing:.2em">maeve@velvetlantern.com.au</div>
</section>

<!-- Business card side 2 -->
<div class="label" style="left:222px;width:252px;top:392px;text-align:center">business card side 2</div>
<section class="sheet card" style="left:222px;top:418px;width:252px;height:145px">
  <div class="damask" role="img" aria-label="Faint damask ornament" style="left:120px;top:6px;width:120px;height:120px"></div>
  <div class="abs caps" style="left:10px;top:18px;font-size:13px">Property Styling</div>
  <div class="abs" style="left:120px;top:41px"><span class="tiny-dot"></span></div>
  <div class="abs caps" style="left:40px;top:58px;font-size:13px">Interior Decorating</div>
  <div class="abs" style="left:120px;top:83px"><span class="tiny-dot"></span></div>
  <div class="abs caps" style="left:98px;top:100px;font-size:13px">Colour Consulting</div>
  <div class="abs center caps" style="left:0;width:252px;top:130px;font-size:9px;letter-spacing:.2em">www.velvetlantern.com.au</div>
</section>

<!-- Letterhead -->
<div class="label" style="left:530px;width:428px;top:16px;text-align:center">letterhead (not to size, but to scale)</div>
<section class="sheet" style="left:530px;top:37px;width:428px;height:553px">
  <div class="brand" style="left:70px;top:42px;font-size:34px"><span>Velvet Lantern</span><span class="mark"></span></div>
  <div class="abs center caps" style="left:0;width:428px;top:92px;font-size:13px;letter-spacing:.16em">22/31-33 Thornbury Rd, Kelvin Grove NSW 2098</div>
  <div class="damask" role="img" aria-label="Large faint damask ornament" style="left:34px;top:130px;width:360px;height:345px"></div>
  <div class="abs caps" style="left:10px;top:456px;font-size:12px;letter-spacing:.2em">Maeve Hollis</div>
  <div class="abs caps" style="left:42px;top:474px;font-size:7px">director</div>
  <div class="abs" style="left:14px;top:484px;font-size:9px;letter-spacing:.25em">p (02)9617 4280</div>
  <div class="abs" style="left:14px;top:498px;font-size:9px;letter-spacing:.25em">m 0427 386 509</div>
  <div class="redline" style="left:134px;top:452px;height:72px"></div>
  <div class="abs center caps" style="left:0;width:428px;top:518px;font-size:12px">maeve@velvetlantern.com.au</div>
  <div class="abs center caps" style="left:0;width:428px;top:534px;font-size:12px">www.velvetlantern.com.au</div>
</section>

<!-- With compliments slip -->
<div class="label" style="left:1016px;top:8px;line-height:16px">compliments<br>(not to size<br>but to scale)</div>
<section class="sheet" style="left:968px;top:60px;width:226px;height:500px">
  <div class="brand" style="left:28px;top:20px;font-size:19px"><span>Velvet Lantern</span><span class="mark"></span></div>
  <div class="abs center caps" style="left:0;width:226px;top:58px;font-size:6.5px;letter-spacing:.1em">22/31-33 Thornbury Rd, Kelvin Grove NSW 2098</div>
  <div class="damask-field" role="img" aria-label="Faint repeating damask pattern" style="left:6px;top:82px;width:214px;height:350px"></div>
  <div class="abs center caps" style="left:0;width:226px;top:94px;font-size:11px">with compliments</div>
  <div class="abs caps" style="left:6px;top:438px;font-size:7px;letter-spacing:.18em">Maeve Hollis</div>
  <div class="abs caps" style="left:26px;top:449px;font-size:5px">director</div>
  <div class="abs" style="left:8px;top:456px;font-size:5.5px;letter-spacing:.18em">p (02)9617 4280</div>
  <div class="abs" style="left:8px;top:465px;font-size:5.5px;letter-spacing:.18em">m 0427 386 509</div>
  <div class="redline" style="left:78px;top:436px;height:38px;width:1px"></div>
  <div class="abs center caps" style="left:0;width:226px;top:476px;font-size:8px;letter-spacing:.2em">maeve@velvetlantern.com.au</div>
  <div class="abs center caps" style="left:0;width:226px;top:487px;font-size:8px;letter-spacing:.2em">www.velvetlantern.com.au</div>
</section>

</body>
</html>
```